Visitenkarten für ein Metallverarbeitsungsbetrieb
Zielgruppe
Metallverarbeitsungsbetrieb
spezialisiert auf Lasern
Aufgabenstellung
Passend zu unseren Logo und in den Farben, schlicht dennoch besonders

```html
<!DOCTYPE html>
<html lang="de">
<head>
<meta charset="utf-8">
<title>Visitenkarte – Vantor Laser GmbH</title>
<link href="https://fonts.googleapis.com/css2?family=Roboto+Condensed:wght@300;400&display=swap" rel="stylesheet">
<style>
  :root {
    --page-bg: #e7ecf0;
    --card-bg: #ffffff;
    --brand-blue: #0a7bb0;
    --text-grey: #5f6062;
  }
  html, body {
    margin: 0;
    padding: 0;
    width: 1200px;
    height: 1200px;
    overflow: hidden;
    background: var(--page-bg);
  }
  .canvas {
    position: relative;
    width: 1200px;
    height: 1200px;
  }
  .business-card {
    position: absolute;
    left: 212px;
    top: 378px;
    width: 775px;
    height: 443px;
    background: var(--card-bg);
    font-family: "Roboto Condensed", "Arial Narrow", sans-serif;
    color: var(--text-grey);
  }
  .person {
    position: absolute;
    left: 77px;
    top: 74px;
  }
  .person-name {
    margin: 0;
    font-size: 48px;
    font-weight: 400;
    line-height: 1;
    color: var(--brand-blue);
    letter-spacing: 0.5px;
  }
  .person-role {
    margin: 12px 0 0;
    font-size: 28px;
    font-weight: 300;
    line-height: 1;
  }
  .contact {
    position: absolute;
    left: 82px;
    top: 218px;
    font-size: 28px;
    font-weight: 300;
    line-height: 34px;
  }
  .contact p { margin: 0; }
  .contact .online {
    margin-top: 14px;
    letter-spacing: 2.5px;
  }
  .company-mark {
    position: absolute;
    left: 442px;
    top: 266px;
    display: flex;
    align-items: center;
    gap: 14px;
  }
  .company-dot {
    width: 44px;
    height: 44px;
    border-radius: 50%;
    background: var(--brand-blue);
  }
  .company-name {
    font-size: 30px;
    font-weight: 400;
    color: var(--text-grey);
    white-space: nowrap;
  }
</style>
</head>
<body>
<div class="canvas">
  <section class="business-card">
    <div class="person">
      <h1 class="person-name">YOUR NAME</h1>
      <p class="person-role">Owner/President</p>
    </div>
    <div class="contact">
      <p>City name, Your Country</p>
      <p>P:&nbsp; (123) 456789</p>
      <div class="online">
        <p>name@yourcompany.de</p>
        <p>www.yourcompany.com</p>
      </div>
    </div>
    <div class="company-mark">
      <span class="company-dot"></span>
      <span class="company-name">Vantor Laser GmbH</span>
    </div>
  </section>
</div>
</body>
</html>
```